Small changes to current design #4574636

********* Please note: This is a one-to-one design project. Sorry for the confusion. I already have a design in mind and this project is being used to modify it. Thank you for your understanding. *********

1. Remove any reference to offshore wind. This event is purely Oil & Gas.
2. Increase header prominence for Products and Services
3. On the locations map could you use a map version which centres on the Middle East please.

If you could make the changes and submit I will review and make the final amendments. In the meantime I will work on the text for the placeholders.

```html
<!DOCTYPE html>
<html lang="en">
<head>
<meta charset="utf-8">
<title>Oil and Natural Gas</title>
<link rel="stylesheet" href="https://fonts.googleapis.com/css2?family=Bebas+Neue&family=Carlito&display=swap">
<style>
  :root {
    --sky-top: #2b5fb8;
    --sky-mid: #1d3f86;
    --sea-deep: #06163a;
    --sea-night: #0a2150;
    --glow-amber: #f2a531;
    --glow-orange: #d9661c;
    --map-blue: #1d47b3;
    --text-white: #ffffff;
  }
  html, body {
    margin: 0;
    padding: 0;
    width: 1200px;
    height: 675px;
    overflow: hidden;
    background: var(--sea-deep);
  }
  .poster {
    position: relative;
    width: 1200px;
    height: 675px;
    overflow: hidden;
    color: var(--text-white);
  }
  .hero-photo {
    position: absolute;
    inset: 0;
    background:
      radial-gradient(ellipse 330px 170px at 600px 330px, rgba(242,165,49,0.85), rgba(217,102,28,0.45) 45%, transparent 75%),
      radial-gradient(ellipse 200px 110px at 840px 270px, rgba(242,165,49,0.7), transparent 70%),
      radial-gradient(ellipse 260px 160px at 1000px 540px, rgba(217,102,28,0.55), transparent 75%),
      radial-gradient(ellipse 70px 40px at 1070px 235px, rgba(255,190,80,0.9), transparent 80%),
      linear-gradient(to bottom, var(--sky-top) 0%, var(--sky-mid) 22%, #24498f 30%, var(--sea-night) 36%, var(--sea-deep) 100%);
  }
  .region-map {
    position: absolute;
    left: 0;
    top: 465px;
    width: 265px;
    height: 210px;
    background: var(--map-blue);
    opacity: 0.9;
    border-radius: 10px 60px 40px 0;
  }
  .headline {
    position: absolute;
    left: 62px;
    top: 42px;
    margin: 0;
    font-family: "Bebas Neue", "Oswald", sans-serif;
    font-weight: 400;
    line-height: 1;
    color: var(--text-white);
  }
  .headline-oil {
    font-size: 172px;
    line-height: 0.82;
    letter-spacing: 1px;
  }
  .headline-and {
    font-size: 74px;
    margin-left: 20px;
    letter-spacing: 1px;
  }
  .headline-gas {
    display: block;
    font-size: 79px;
    line-height: 0.9;
    margin-top: 2px;
    letter-spacing: 0.5px;
  }
  .intro-copy {
    position: absolute;
    left: 494px;
    top: 462px;
    width: 680px;
    margin: 0;
    font-family: "Carlito", "Calibri", sans-serif;
    font-size: 19px;
    line-height: 22px;
    color: var(--text-white);
  }
  .intro-line {
    display: block;
    white-space: nowrap;
    text-align: justify;
    text-align-last: justify;
  }
  .intro-line.short {
    width: 634px;
  }
  .intro-line.last {
    text-align-last: left;
  }
</style>
</head>
<body>
  <main class="poster">
    <div class="hero-photo" role="img" aria-label="Photograph of a brightly lit offshore oil and gas platform at dusk, with a gas flare and reflections on the sea under a blue sky"></div>
    <div class="region-map" role="img" aria-label="Map of the Middle East region"></div>

    <h1 class="headline">
      <span class="headline-oil">Oil</span><span class="headline-and">and</span>
      <span class="headline-gas">Natural Gas</span>
    </h1>

    <p class="intro-copy" lang="la">
      <span class="intro-line short">This is Layerset's version of Lorem Ipsum. Proin gravida nibh vel velit</span>
      <span class="intro-line">auctor aliquet. Aenean sollicitudin, lorem quis bibendum auctor, nisi elit con-</span>
      <span class="intro-line">sequat ipsum, nec sagittis sem nibh id elit. Duis sed odio sit amet nibh vulpu-</span>
      <span class="intro-line">tate cursus a sit amet mauris. Morbi accumsan ipsum velit. Nam nec tellus a</span>
      <span class="intro-line short">odio tincidunt auctor a ornare odio. Sed non mauris vitae erat consequat</span>
      <span class="intro-line">auctor eu in elit. Class aptent taciti sociosqu ad litora torquent per conubia</span>
      <span class="intro-line">nostra, per inceptos himenaeos. Mauris in erat justo. Nullam ac urna eu felis</span>
      <span class="intro-line last">dapibus condimentum sit amet a augue. Sed non neque elit. Sed ut imperdiet.</span>
    </p>
  </main>
</body>
</html>
```